Bright Fern Painting needs a new business card. See attachments for our logo and current card as an example.
We want to utilize the same colors in the logo, and keep all the information that is currently on it. Just need an updated and modern design.
We are open to loosing the Association Logos if it means a better design.
We are also entertaining a spot for a picture of a headshot of the person listed on the card. Head shot can be finished later.

```html
<!DOCTYPE html>
<html lang="en">
<head>
<meta charset="utf-8">
<title>Bright Fern Painting – Business Card</title>
<link rel="stylesheet" href="https://fonts.googleapis.com/css2?family=Roboto:wght@300;400;500;700&display=swap">
<style>
  :root {
    --fern-green: #3e4632;
    --brick-maroon: #6b3935;
    --card-white: #ffffff;
    --stage-grey: #6d6e70;
    --ink-white: #ffffff;
  }
  * { box-sizing: border-box; margin: 0; padding: 0; }
  html, body {
    width: 1028px; height: 1200px; overflow: hidden;
    background: var(--stage-grey);
    font-family: "Roboto", Arial, sans-serif;
  }
  .canvas { position: relative; width: 1028px; height: 1200px; }

  .card {
    position: absolute; left: 78px; width: 877px; height: 500px;
    background: var(--card-white);
    box-shadow: 6px 10px 18px rgba(0,0,0,0.35);
    overflow: hidden;
  }
  .card--front { top: 83px; }
  .card--back { top: 605px; }

  /* Front */
  .front-brand {
    position: absolute; left: 0; right: 0; top: 215px;
    text-align: center;
    font-size: 52px; font-weight: 700; color: var(--fern-green);
    letter-spacing: 0.5px;
  }
  .front-band {
    position: absolute; left: 0; right: 0; bottom: 0; height: 84px;
    background: var(--fern-green);
  }
  .front-url {
    position: absolute; left: 0; right: 0; top: 12px;
    text-align: center; color: var(--ink-white);
    font-size: 21px; font-weight: 400; letter-spacing: 3.6px;
  }

  /* Back */
  .back-panel {
    position: absolute; left: 0; top: 0; width: 467px; height: 100%;
    background: var(--fern-green); color: var(--ink-white);
  }
  .name-tab {
    position: absolute; left: 0; top: 117px; width: 31px; height: 75px;
    background: var(--brick-maroon);
  }
  .person-name {
    position: absolute; left: 61px; top: 122px;
    font-size: 30px; font-weight: 500; letter-spacing: 2.6px;
  }
  .person-role {
    position: absolute; left: 61px; top: 160px;
    font-size: 20px; font-weight: 300; letter-spacing: 1.6px;
  }
  .contact-list { position: absolute; left: 60px; top: 338px; list-style: none; }
  .contact-item {
    display: flex; align-items: center; height: 34px; margin-bottom: 15px;
    font-size: 21px; font-weight: 300; letter-spacing: 1.8px;
  }
  .contact-icon { width: 36px; height: 36px; margin-right: 22px; flex: none; }

  .back-brand {
    position: absolute; left: 467px; width: 395px; top: 162px;
    text-align: center;
    font-size: 28px; font-weight: 700; color: var(--fern-green);
  }
  .services {
    position: absolute; left: 509px; top: 349px;
    font-size: 21px; font-weight: 400; color: var(--fern-green);
    line-height: 39px;
  }
  .service-row { display: grid; grid-template-columns: 180px auto; white-space: nowrap; }
  .service-row span:last-child::before { content: "● "; font-size: 17px; }
  .edge-strip {
    position: absolute; right: 0; top: 0; width: 15px; height: 100%;
    background: var(--brick-maroon);
  }
</style>
</head>
<body>
<div class="canvas">

  <section class="card card--front">
    <div class="front-brand">Bright Fern Painting</div>
    <div class="front-band">
      <div class="front-url">www.brightfernpainting.com</div>
    </div>
  </section>

  <section class="card card--back">
    <div class="back-panel">
      <div class="name-tab"></div>
      <div class="person-name">DANIEL HARPER</div>
      <div class="person-role">Quality Manager</div>
      <ul class="contact-list">
        <li class="contact-item">
          <svg class="contact-icon" viewBox="0 0 36 36" aria-hidden="true">
            <circle cx="18" cy="18" r="16.5" fill="none" stroke="#fff" stroke-width="2"/>
            <path d="M12.5 10.5c1-1 2-1 2.6 0l1.6 2.6c.5.8.3 1.6-.4 2.2l-1 .8c.8 2 2.5 3.8 4.6 4.6l.8-1c.6-.7 1.4-.9 2.2-.4l2.6 1.6c1 .6 1 1.6 0 2.6l-1.2 1.2c-1 1-2.6 1.2-4 .6-4-1.8-7.2-5-9-9-.6-1.4-.4-3 .6-4z" fill="#fff"/>
          </svg>
          262 555 0147
        </li>
        <li class="contact-item">
          <svg class="contact-icon" viewBox="0 0 36 36" aria-hidden="true">
            <circle cx="18" cy="18" r="16.5" fill="none" stroke="#fff" stroke-width="2"/>
            <rect x="10" y="12.5" width="16" height="11" rx="1" fill="#fff"/>
            <path d="M10.5 13.3l7.5 5.6 7.5-5.6M10.5 23l5.6-4.6M25.5 23l-5.6-4.6" fill="none" stroke="#3e4632" stroke-width="1.2"/>
          </svg>
          daniel.brightfern@mail.com
        </li>
      </ul>
    </div>

    <div class="back-brand">Bright Fern Painting</div>

    <div class="services">
      <div class="service-row"><span>Exterior Painting</span><span>Carpentry</span></div>
      <div class="service-row"><span>Interior Painting</span><span>Drywall</span></div>
    </div>

    <div class="edge-strip"></div>
  </section>

</div>
</body>
</html>
```